Stationery for a professional investment company

Hi, I would like to design full stationary set based on my logo. I would like to use the red color in the file as well as white.

The design should be simple, credible and serious.

Q7 manages portfolio companies. The companies that represent our industry are

LMW (https://www.lmw-example.com)

RNB Capital

Target Market(s)

Investment professionals

Industry/Entity Type

Investment Advisory

Font styles to use
Sans Serif

Colors
ec1f27

Requirements
Must have
• A4 Letterhead, C4 envelop, C5 envelop, DL envelop

```html
<!DOCTYPE html>
<html lang="en">
<head>
<meta charset="utf-8">
<title>Q7 – Letterhead</title>
<link href="https://fonts.googleapis.com/css2?family=Open+Sans:wght@400;600&display=swap" rel="stylesheet">
<style>
  :root {
    --brand-red: #9a1f26;
    --charcoal: #3a3a3d;
    --paper: #ffffff;
    --backdrop: #d9dcdd;
    --muted-text: #6b6b6e;
  }
  html, body {
    margin: 0;
    width: 1200px;
    height: 784px;
    overflow: hidden;
    background: var(--backdrop);
  }
  .letterhead {
    position: absolute;
    left: 338px;
    top: 22px;
    width: 523px;
    height: 740px;
    background: var(--paper);
    box-shadow: 0 2px 10px rgba(0,0,0,0.12);
    overflow: hidden;
  }
  .corner-mark {
    position: absolute;
    width: 4px;
    height: 34px;
  }
  .corner-mark--gray-left { left: 0; top: 0; background: var(--charcoal); }
  .corner-mark--red-left { left: 9px; top: 34px; background: var(--brand-red); }
  .corner-mark--gray-right { right: 0; top: 0; background: var(--charcoal); }
  .corner-mark--red-right { right: 9px; top: 34px; background: var(--brand-red); }

  .brand-name {
    position: absolute;
    left: 48px;
    top: 30px;
    margin: 0;
    display: flex;
    align-items: center;
    gap: 8px;
    font-family: "Open Sans", sans-serif;
    font-weight: 600;
    font-size: 26px;
    line-height: 1;
    color: var(--brand-red);
  }
  .brand-square {
    width: 14px;
    height: 14px;
    background: var(--brand-red);
  }

  .contact-block {
    position: absolute;
    right: 32px;
    top: 34px;
    margin: 0;
    padding: 0;
    list-style: none;
    font-family: "Open Sans", sans-serif;
    font-size: 9px;
    line-height: 13px;
  }
  .contact-item {
    display: flex;
    align-items: flex-start;
    gap: 5px;
  }
  .contact-item svg { flex: none; margin-top: 2px; }
  .contact-item--address { color: var(--brand-red); font-weight: 600; }
  .contact-item--phone,
  .contact-item--web { color: var(--muted-text); }

  .footer-rule {
    position: absolute;
    left: 0;
    right: 0;
    bottom: 0;
    height: 20px;
  }
  .footer-rule span { position: absolute; }
  .rule-thin { bottom: 14px; height: 3px; }
  .rule-thin--red-a { left: 0; width: 27%; background: var(--brand-red); }
  .rule-thin--gray { left: 28%; width: 34%; background: var(--charcoal); }
  .rule-thin--red-b { left: 63%; right: 0; background: var(--brand-red); }
  .rule-band { bottom: 0; height: 9px; }
  .rule-band--red { left: 0; width: 73%; background: var(--brand-red); }
  .rule-band--gray { left: 73%; right: 0; background: linear-gradient(90deg, var(--charcoal), #1f1f21); }
</style>
</head>
<body>
  <main class="letterhead">
    <span class="corner-mark corner-mark--gray-left"></span>
    <span class="corner-mark corner-mark--red-left"></span>
    <span class="corner-mark corner-mark--gray-right"></span>
    <span class="corner-mark corner-mark--red-right"></span>

    <h1 class="brand-name"><span class="brand-square"></span>Q7</h1>

    <ul class="contact-block">
      <li class="contact-item contact-item--address">
        <svg width="9" height="9" viewBox="0 0 10 10"><circle cx="5" cy="5" r="4.5" fill="var(--brand-red)"/><path d="M5 2.3a1.7 1.7 0 0 0-1.7 1.7C3.3 5.3 5 7.6 5 7.6S6.7 5.3 6.7 4A1.7 1.7 0 0 0 5 2.3z" fill="#fff"/></svg>
        <span>LMW 12 Harbor Lane Suite<br>300 Riverton 10521</span>
      </li>
      <li class="contact-item contact-item--phone">
        <svg width="9" height="9" viewBox="0 0 10 10"><circle cx="5" cy="5" r="4.3" fill="none" stroke="var(--brand-red)" stroke-width="1"/><path d="M3.6 2.9l0.9 0.9-0.5 0.7c0.3 0.6 0.8 1.1 1.4 1.4l0.7-0.5 0.9 0.9-0.6 0.8C5 6.9 3.1 5 3 3.5z" fill="var(--brand-red)"/></svg>
        <span>+ 1 (555) 014-2270</span>
      </li>
      <li class="contact-item contact-item--web">
        <svg width="9" height="9" viewBox="0 0 10 10"><circle cx="5" cy="5" r="4.5" fill="var(--brand-red)"/><circle cx="5" cy="5" r="2.6" fill="none" stroke="#fff" stroke-width="0.8"/><path d="M2.4 5h5.2M5 2.4v5.2" stroke="#fff" stroke-width="0.6"/></svg>
        <span>https://www.lmw-example.com</span>
      </li>
    </ul>

    <div class="footer-rule">
      <span class="rule-thin rule-thin--red-a"></span>
      <span class="rule-thin rule-thin--gray"></span>
      <span class="rule-thin rule-thin--red-b"></span>
      <span class="rule-band rule-band--red"></span>
      <span class="rule-band rule-band--gray"></span>
    </div>
  </main>
</body>
</html>
```